Business Card for Coastline Keel

Hello, Will you do a business card design for Coastline Keel? I attached a card from an old business of mine that I would like to copy.

The new info is:
Dylan Forsey
Owner
251-555-0187

Adress is:
41730 Heron Way, Orange Beach AL 36561

Email: dylan@coastlinekeelandfuel.example

Website is: www.coastlinekeelandfuel.example

Contact Information for Business Card

Please use the new coastline keel logo

Requirements
Must have
• QR Code for contact information

```html
<!DOCTYPE html>
<html lang="en">
<head>
<meta charset="utf-8">
<title>Coastline Keel – Business Card</title>
<link rel="stylesheet" href="https://fonts.googleapis.com/css2?family=Archivo:wght@500;600;700;800&display=swap">
<style>
  :root {
    --backdrop: #dfe2e6;
    --card: #ffffff;
    --ink: #141414;
    --brand-blue: #1a78c2;
    --code-tone: #4a4d52;
  }
  * { margin: 0; padding: 0; box-sizing: border-box; }
  html, body {
    width: 1200px;
    height: 1200px;
    overflow: hidden;
    background: var(--backdrop);
    font-family: "Archivo", Arial, sans-serif;
    color: var(--ink);
  }
  .card {
    position: absolute;
    left: 305px;
    width: 590px;
    height: 336px;
    background: var(--card);
  }
  .card--front { top: 216px; }
  .card--back { top: 647px; }

  .brand {
    position: absolute;
    display: flex;
    align-items: center;
    white-space: nowrap;
  }
  .brand__dot {
    border-radius: 50%;
    background: var(--ink);
    flex: none;
  }
  .brand__name {
    font-weight: 800;
    color: var(--ink);
    letter-spacing: -0.5px;
    line-height: 1;
  }
  .card--front .brand {
    left: 0; right: 0; top: 132px;
    justify-content: center;
    gap: 18px;
  }
  .card--front .brand__dot { width: 76px; height: 76px; }
  .card--front .brand__name { font-size: 44px; }

  .card--back .brand {
    left: 49px; top: 84px;
    gap: 10px;
  }
  .card--back .brand__dot { width: 44px; height: 44px; }
  .card--back .brand__name { font-size: 25px; }

  .contact-code {
    position: absolute;
    left: 49px;
    top: 146px;
    width: 84px;
    height: 84px;
    background: var(--code-tone);
  }

  .person {
    position: absolute;
    right: 49px;
    top: 107px;
    text-align: right;
  }
  .person__name {
    font-size: 31px;
    font-weight: 600;
    color: var(--brand-blue);
    line-height: 1.1;
  }
  .person__title {
    font-size: 19px;
    font-weight: 500;
    line-height: 1.2;
  }
  .phone {
    position: absolute;
    right: 49px;
    top: 186px;
    display: flex;
    align-items: center;
    gap: 10px;
    font-size: 20px;
    font-weight: 600;
    color: var(--brand-blue);
  }
  .phone svg { width: 17px; height: 17px; fill: var(--brand-blue); }

  .contact-line {
    display: flex;
    align-items: center;
    gap: 5px;
    font-size: 13px;
    font-weight: 500;
    line-height: 18px;
  }
  .contact-line svg { width: 13px; height: 13px; fill: var(--ink); flex: none; }

  .address {
    position: absolute;
    left: 48px;
    top: 248px;
  }
  .address .indent { padding-left: 18px; }

  .online {
    position: absolute;
    right: 49px;
    top: 248px;
  }
  .online .contact-line { justify-content: flex-end; }
</style>
</head>
<body>

<section class="card card--front">
  <div class="brand">
    <span class="brand__dot"></span>
    <span class="brand__name">COASTLINE KEEL</span>
  </div>
</section>

<section class="card card--back">
  <div class="brand">
    <span class="brand__dot"></span>
    <span class="brand__name">COASTLINE KEEL</span>
  </div>

  <div class="contact-code" role="img" aria-label="QR code linking to contact information"></div>

  <div class="person">
    <p class="person__name">Dylan Forsey</p>
    <p class="person__title">Owner</p>
  </div>

  <p class="phone">
    <svg viewBox="0 0 24 24" aria-hidden="true"><path d="M6.6 10.8a15.1 15.1 0 0 0 6.6 6.6l2.2-2.2a1 1 0 0 1 1-.25 11.4 11.4 0 0 0 3.6.57 1 1 0 0 1 1 1V20a1 1 0 0 1-1 1A17 17 0 0 1 3 4a1 1 0 0 1 1-1h3.5a1 1 0 0 1 1 1c0 1.25.2 2.45.57 3.57a1 1 0 0 1-.25 1z"/></svg>
    251-555-0187
  </p>

  <div class="address">
    <p class="contact-line">
      <svg viewBox="0 0 24 24" aria-hidden="true"><path d="M12 2a7 7 0 0 0-7 7c0 5.2 7 13 7 13s7-7.8 7-13a7 7 0 0 0-7-7zm0 9.5A2.5 2.5 0 1 1 12 6.5a2.5 2.5 0 0 1 0 5z"/></svg>
      41730 Heron Way
    </p>
    <p class="contact-line indent">Orange Beach, AL 36561</p>
  </div>

  <div class="online">
    <p class="contact-line">
      <svg viewBox="0 0 24 24" aria-hidden="true"><path d="M2 5h20v14H2zm2 2v.5l8 5 8-5V7z"/></svg>
      dylan@coastlinekeelandfuel.example
    </p>
    <p class="contact-line">
      <svg viewBox="0 0 24 24" aria-hidden="true"><path d="M5 2l14 12h-7l4 8-3 1.5-4-8L5 20z"/></svg>
      www.coastlinekeelandfuel.example
    </p>
  </div>
</section>

</body>
</html>
```